Etiketten-Design für Honiggläser
Die Zusammenarbeit mit Jorin war sehr unkompliziert. Änderungswünsche wurden prompt umgesetzt und die Beratung war hervorragend! Besten Dank für das tolle Etikett!
Zielgruppe
Wir sind Imker und benötigen Etiketten für Honiggläser.
Aufgabenstellung
Siehe Anlage. Es sollen keine Fotos verwendet werden. Grafiken sind in Ordnung.
Etiketten-Design für Honigglas Etiketten-Design für Honigglas"
Format: Etikett für 250-gr.-Honigglas (TO ∅ 63 mm). Standardmaßgrösse 165 × 40 mm Design: schlicht, hochwertig, modern, edel/royal, unkonventionelles Design (weg von Bienen, Waben, Landschaften usw.), dunkle Farbtöne in Kontrast zu heller Schrift, die beiden Textbausteine 'Los Nr. ' sowi..
Attraktives Etiketten-Design für Honig Attraktives Etiketten-Design für Honig"
Wir verkaufen zur Zeit vor allem Waldhonig, streben aber auch einen Blütenhonig an. Das Etikett soll daher entweder den Wald wiederspiegeln oder aber neutral sein, so dass der Schriftzug Waldhonig oder Blütenhonig jeweils eingesetzt werden kann. Wichtig ist mir der Ortszusatz 'aus dem Glottertal..
Etiketten-Design für Produkte eines Familienbetriebs mit Imkerei und Hühnerhaltung Etiketten-Design für Produkte eines Familienbetriebs mit Imkerei und Hühnerhaltung"
1. Zentrale, auf allen Etiketten wiederkehrende Elemente: - Unser Riegelhaus (stilisiert) (Bild beiliegend) - Das Wort 'Weidlek' (Anmerkung: ohne Anführungszeichen) - die zentralen Elemente sollen die Produkte nicht überragen. 2. Dezente Adresse: - Familie Rattinger, Mühlgrund, CH-9617 Brüsel 3...
Etiketten-Design für Kurkuma-Honig Etiketten-Design für Kurkuma-Honig"
Etikett für 500g // Stanze eckig (210x35mm), Druckdatei entsprechend Vorgaben https://klebwerkstatt.de/faq/ Vorgaben für das Grünfeld Logo im Anhang Vorgaben für EG Öko Logo : https://oekosiegel-muster.eu/landbau/organic/downloads/logo_de Pflichtangaben auf dem Etikett: Gewicht, Adresse siehe Beispiel..
Etiketten-Design für Blütenhonig und Waldhonig gesucht Etiketten-Design für Blütenhonig und Waldhonig gesucht"
Zwei verschiedene Etiketten-Desings 1 x Blütenhonig sowie 1 x Waldhonig für unterschiedliche Honigglasgrößen (500 g und 250 g) Die Maße für die Etiketten wären: Für 500-Gramm-Glas 210 mm x 45 mm für's 250-Gramm-Glas 180 mm x 38 mm. Wir sind auch offen für neue Vorschläge bezüglich ..

```html
<!DOCTYPE html>
<html lang="de">
<head>
<meta charset="utf-8">
<title>Etikett Spättracht Waldhonig</title>
<link href="https://fonts.googleapis.com/css2?family=Cinzel:wght@400&family=Encode+Sans+Condensed:wght@400;500&family=Montserrat:wght@500&family=Kaushan+Script&display=swap" rel="stylesheet">
<style>
  :root {
    --black: #000000;
    --label-bg: #121212;
    --gold: #b9a45c;
    --honey: #f2c318;
    --green: #6cc417;
    --white: #ffffff;
    --faint: #2a2a2a;
  }
  * { margin: 0; padding: 0; box-sizing: border-box; }
  html, body { width: 1006px; height: 1200px; overflow: hidden; background: var(--white); }
  .canvas { position: relative; width: 1006px; height: 1200px; }

  .lid-strip {
    position: absolute; left: 389px; top: 0; width: 232px; height: 776px;
    background: var(--black); overflow: hidden;
  }
  .comb-area { position: absolute; }
  .lid-strip .comb-top {
    left: 0; top: 0; width: 232px; height: 282px;
    background: linear-gradient(160deg, #1a1406 0%, #000 55%, #1a1406 100%);
  }
  .lid-strip .comb-bottom {
    left: 0; top: 525px; width: 232px; height: 251px;
    background: linear-gradient(200deg, #1a1406 0%, #000 50%, #1a1406 100%);
  }
  .date-box {
    position: absolute; left: 38px; top: 24px; width: 166px; height: 76px;
    background: var(--white);
    display: flex; align-items: flex-start; justify-content: center;
    transform: rotate(180deg);
  }
  .date-box span {
    font-family: "Encode Sans Condensed", sans-serif; font-size: 14px; color: var(--black);
    margin-top: 4px;
  }
  .lid-brand {
    position: absolute; left: 0; top: 330px; width: 232px; text-align: center;
    font-family: "Cinzel", serif; color: var(--white); font-size: 37px; line-height: 36px;
  }
  .brand-dot {
    display: block; width: 64px; height: 64px; border-radius: 50%;
    background: var(--honey); margin: 0 auto 28px;
  }

  .main-label {
    position: absolute; left: 0; top: 775px; width: 1006px; height: 425px;
    background: var(--label-bg); overflow: hidden;
  }
  .accent-line { position: absolute; left: 0; top: 17px; width: 1006px; height: 11px; background: var(--green); }
  .main-label .comb-left {
    left: 0; top: 168px; width: 406px; height: 210px;
    background: linear-gradient(90deg, #2b2410 0%, #1b170c 60%, var(--label-bg) 100%);
  }
  .main-label .comb-right {
    left: 603px; top: 195px; width: 403px; height: 183px;
    background: linear-gradient(270deg, #2b2410 0%, #1b170c 60%, var(--label-bg) 100%);
  }
  .info-text {
    position: absolute; font-family: "Encode Sans Condensed", sans-serif;
    color: var(--gold); text-align: center; font-size: 22px; line-height: 27.5px;
  }
  .info-crystal { left: 12px; top: 41px; width: 300px; }
  .info-storage { left: 700px; top: 44px; width: 300px; }
  .best-before {
    position: absolute; left: 740px; top: 11px; font-family: "Encode Sans Condensed", sans-serif;
    font-size: 15px; line-height: 16px; color: var(--faint);
  }
  .center-brand {
    position: absolute; left: 300px; top: 148px; width: 406px; text-align: center;
    font-family: "Cinzel", serif; color: var(--honey); font-size: 30px;
  }
  .region {
    position: absolute; left: 300px; top: 186px; width: 406px; text-align: center;
    font-family: "Encode Sans Condensed", sans-serif; color: var(--faint); font-size: 21px;
  }
  .fill-amount {
    position: absolute; left: 720px; top: 166px; width: 180px; text-align: center;
    font-family: "Montserrat", sans-serif; color: var(--gold); font-size: 29px; line-height: 34px;
  }
  .variety-banner { position: absolute; left: 300px; top: 212px; width: 420px; height: 130px; }
  .variety-name {
    position: absolute; left: 385px; top: 222px; width: 240px; text-align: center;
    font-family: "Kaushan Script", cursive; font-size: 40px; color: var(--black); transform: rotate(-3deg);
  }
  .variety-type {
    position: absolute; left: 410px; top: 268px; width: 200px; text-align: center;
    font-family: "Encode Sans Condensed", sans-serif; font-weight: 500; font-size: 25px; color: var(--black);
  }
  .footer-line {
    position: absolute; top: 382px; font-family: "Encode Sans Condensed", sans-serif;
    color: var(--white); font-size: 22px;
  }
  .footer-address { left: 9px; }
  .footer-mail { right: 51px; }
</style>
</head>
<body>
<div class="canvas">
  <section class="lid-strip">
    <div class="comb-area comb-top" role="img" aria-label="Goldenes Wabenmuster auf Schwarz"></div>
    <div class="comb-area comb-bottom" role="img" aria-label="Goldenes Wabenmuster auf Schwarz"></div>
    <div class="date-box"><span>Mindestens haltbar bis</span></div>
    <div class="lid-brand"><span class="brand-dot"></span>Imkerei<br>Brandauer</div>
  </section>

  <section class="main-label">
    <div class="accent-line"></div>
    <div class="comb-area comb-left" role="img" aria-label="Goldenes Wabenmuster"></div>
    <div class="comb-area comb-right" role="img" aria-label="Goldenes Wabenmuster"></div>

    <p class="info-text info-crystal">Bienenhonig kristallisiert bei län-<br>gerer Lagerung. Durch Erwärmen<br>im Wasserbad bei 40°C kann Honig<br>ohne Schaden wieder verflüssigt<br>werden.</p>

    <p class="best-before">mindestens<br>haltbar bis:</p>
    <p class="info-text info-storage">Lagerhinweis:<br>Kühl, dunkel und trocken lagern.<br>Mehrwegglas:<br>Bitte zurück zum Imker</p>

    <div class="center-brand">Imkerei Brandauer</div>
    <div class="region">Bayerischer Bienenhonig</div>

    <div class="fill-amount">Füllmenge<br>500 g</div>

    <svg class="variety-banner" viewBox="0 0 420 130" aria-hidden="true">
      <path d="M6 12 C 120 -6, 260 30, 380 42 L 416 52 C 392 70, 372 96, 362 122 C 250 98, 120 118, 8 110 C 2 80, 2 40, 6 12 Z" fill="#6cc417"/>
      <path d="M20 14 C 130 4, 260 30, 370 50 C 385 56, 392 62, 396 70" fill="none" stroke="#000" stroke-width="2.5"/>
      <path d="M20 104 C 120 110, 250 94, 352 112" fill="none" stroke="#000" stroke-width="1.5"/>
    </svg>
    <div class="variety-name">Spättracht</div>
    <div class="variety-type">Waldhonig</div>

    <p class="footer-line footer-address">Imkerei Brandauer • Lindenanger 14 • 85999 Hollerbach</p>
    <p class="footer-line footer-mail">E-Mail: info@imkerei-brandauer.de</p>
  </section>
</div>
</body>
</html>
```